Online retailer needs a Quirky yet professionally designed double sided business car

We mainly sell kitchen and home accessories but pretty much anything new and in demand. Have a look at our site and then come up with designs.
Design to be really catching and want people to visit the website.
Final details such as number, director name and email address will be given to the designer of the winning business card.

Www.zapfinda.com

Ideas out of the norm also welcome!!

```html
<!DOCTYPE html>
<html lang="en">
<head>
<meta charset="utf-8">
<title>Zapfinda – Business Card</title>
<link rel="stylesheet" href="https://fonts.googleapis.com/css2?family=Questrial&family=Montserrat:wght@600&display=swap">
<style>
  :root {
    --backdrop: #d9d4cd;
    --card: #f2f0ed;
    --card-edge: #d4d0ca;
    --ink: #2b2b2b;
    --ink-soft: #4a4a4a;
    --accent: #e07b2c;
    --rule: #8a8a8a;
    --mark: #e3e0dc;
  }
  * { margin: 0; padding: 0; box-sizing: border-box; }
  html, body {
    width: 1200px;
    height: 970px;
    overflow: hidden;
    background: var(--backdrop);
  }
  .card {
    position: absolute;
    left: 75px;
    top: 193px;
    width: 1050px;
    height: 584px;
    background: var(--card);
    border: 1px solid var(--card-edge);
    box-shadow: 0 6px 24px rgba(0,0,0,0.12);
    overflow: hidden;
  }
  .brand {
    position: absolute;
    left: 88px;
    top: 96px;
    width: 390px;
  }
  .brand-name {
    font-family: "Questrial", sans-serif;
    font-size: 66px;
    line-height: 1;
    color: var(--ink);
    letter-spacing: 1px;
  }
  .tagline {
    display: flex;
    align-items: center;
    gap: 10px;
    margin-top: 8px;
    font-family: "Questrial", sans-serif;
    font-size: 18px;
    color: var(--accent);
    white-space: nowrap;
  }
  .tagline::before,
  .tagline::after {
    content: "";
    flex: 1;
    height: 1px;
    background: var(--rule);
  }
  .person {
    position: absolute;
    left: 88px;
    top: 316px;
    font-family: "Montserrat", sans-serif;
    font-weight: 600;
    font-size: 22px;
    letter-spacing: 4px;
    color: var(--ink-soft);
  }
  .contacts {
    position: absolute;
    left: 90px;
    top: 408px;
    list-style: none;
  }
  .contacts li {
    display: flex;
    align-items: center;
    height: 36.5px;
    font-family: "Questrial", sans-serif;
    font-size: 19px;
    letter-spacing: 2px;
    color: var(--ink-soft);
  }
  .contacts svg {
    width: 22px;
    height: 22px;
    margin-right: 36px;
    fill: none;
    stroke: var(--accent);
    stroke-width: 1.8;
  }
  .contacts .web { font-weight: 600; font-family: "Montserrat", sans-serif; font-size: 17px; }
  .contacts .web span { color: var(--accent); }
  .brand-mark {
    position: absolute;
    left: 611px;
    top: 107px;
    width: 418px;
    height: 418px;
    border-radius: 50%;
    background: var(--mark);
  }
</style>
</head>
<body>
  <div class="card">
    <div class="brand">
      <div class="brand-name">Zapfinda</div>
      <div class="tagline">gadgets for every home</div>
    </div>

    <div class="person">MARA LENN</div>

    <ul class="contacts">
      <li>
        <svg viewBox="0 0 24 24" aria-hidden="true"><path d="M4 9c0-3 4-4 8-4s8 1 8 4v2h-4V9H8v2H4z"/><rect x="6" y="12" width="12" height="7" rx="1"/></svg>
        06 12 34 56 78
      </li>
      <li>
        <svg viewBox="0 0 24 24" aria-hidden="true"><rect x="3" y="6" width="18" height="12"/><path d="M3 6l9 7 9-7"/></svg>
        mara@zapfinda.com
      </li>
      <li>
        <svg viewBox="0 0 24 24" aria-hidden="true"><circle cx="12" cy="12" r="9"/><path d="M3 12h18M12 3c3 3 3 15 0 18M12 3c-3 3-3 15 0 18"/></svg>
        <span class="web">www.<span>zapfinda</span>.com</span>
      </li>
    </ul>

    <div class="brand-mark" aria-hidden="true"></div>
  </div>
</body>
</html>
```